PELMIR - Letterhead

Brightwater Institute of Letters and Crafts (PELMIR) is a non-profit organization that operates two tuition-free public schools - PELMIR Elementary for grades K to 5th and PELMIR College Prep for grades 6-12.

We are looking for a letterhead primarily to be used on Google Docs and Microsoft Word. Attached are two versions of our logo. One with our name spelled out and one with the acronym.

For Letterhead, we would like 3 addresses listed:

PELMIR HQ
41827 Heron Bluff Lane, Suite 316
Laguna Niguel, CA 92677

PELMIR Elementary (K-5)
57314 Marbleton Ridge Road
Laguna Niguel, CA 92677

PELMIR College Prep (6-12)
46803 Sable Creek Way
San Juan Capistrano, CA 92675

Our Phone Number is (949) 555-0147
Our Fax Number is the same (949) 555-0147

Our website is www.pelmir-learn.example

Target Market(s)

Education

Industry/Entity Type

Education

Font styles to use
Sans Serif

Colors
0054AA
0677BA
7BADD7
CADEEF
E8F1F8

Requirements
Must have
• Logo, Address, Phone Number, Website.
Nice to have
• Modern and clean design.
Should not have
• Prefer that there is no bleed -- the letterhead will mostly be used in PDF format however sometimes it will be printed and our printers can not do a full bleed

```html
<!DOCTYPE html>
<html lang="en">
<head>
<meta charset="utf-8">
<title>PELMIR Letterhead</title>
<link href="https://fonts.googleapis.com/css2?family=Arimo:wght@400;700&display=swap" rel="stylesheet">
<style>
  :root {
    --backdrop: #e9e9e9;
    --paper: #ffffff;
    --ink: #1d1d1f;
    --brand-blue: #1b47a0;
    --sky: #1f8ad6;
    --green: #1fa84a;
    --yellow: #f4cf1b;
    --orange: #f15a36;
    --sign-tone: #d4d8e0;
  }
  * { box-sizing: border-box; margin: 0; padding: 0; }
  html, body { width: 1200px; height: 874px; overflow: hidden; }
  body {
    background: var(--backdrop);
    font-family: "Arimo", Arial, sans-serif;
    color: var(--ink);
    position: relative;
  }
  .letterhead {
    position: absolute;
    left: 291px; top: 37px;
    width: 618px; height: 800px;
    background: var(--paper);
    box-shadow: 0 6px 24px rgba(0,0,0,.12);
    overflow: hidden;
  }
  .brand {
    position: absolute; left: 52px; top: 58px;
    display: flex; align-items: center; gap: 10px;
  }
  .brand-dot { width: 26px; height: 26px; border-radius: 50%; background: var(--brand-blue); }
  .brand-name {
    font-weight: 700; font-size: 17px; line-height: 1.15; color: var(--brand-blue);
  }
  .contact {
    position: absolute; right: 52px; top: 58px;
    display: flex; align-items: center; gap: 14px;
    font-size: 9px; line-height: 1.7;
  }
  .contact-rule { width: 26px; height: 1.5px; background: var(--orange); }
  .contact-line { display: flex; align-items: center; gap: 5px; }
  .contact-line svg { width: 10px; height: 10px; }
  .letter {
    position: absolute; left: 52px; right: 52px; top: 150px;
    font-size: 10.5px; line-height: 1.45;
  }
  .recipient { margin-bottom: 14px; }
  .letter p { margin-bottom: 14px; }
  .closing { margin-top: 4px; }
  .signature-area {
    width: 120px; height: 44px; margin-top: 8px; border-radius: 6px;
    background: linear-gradient(90deg, var(--sign-tone), #eef0f4);
  }
  .locations {
    position: absolute; left: 52px; right: 40px; bottom: 88px;
    display: flex; gap: 22px;
    font-size: 9px; line-height: 1.45;
  }
  .location { padding-left: 12px; border-left: 1px solid var(--brand-blue); }
  .location:first-child { border-left: none; padding-left: 0; width: 170px; }
  .footer { position: absolute; left: 0; bottom: 0; width: 618px; height: 72px; }
  .website {
    position: absolute; left: 28px; bottom: 16px;
    display: flex; align-items: center; gap: 6px;
    color: #fff; font-size: 11px;
  }
  .website svg { width: 11px; height: 11px; }
</style>
</head>
<body>
  <main class="letterhead">
    <header class="brand">
      <span class="brand-dot"></span>
      <div class="brand-name">Brightwater Institute<br>of Letters and Crafts</div>
    </header>

    <div class="contact">
      <span class="contact-rule"></span>
      <div>
        <div class="contact-line">
          <svg viewBox="0 0 10 10"><circle cx="5" cy="5" r="5" fill="#1b47a0"/><path d="M3.2 2.6l1 1-.6.7c.4.8 1 1.4 1.8 1.8l.7-.6 1 1-.8.8C4.6 7.1 2.9 5.4 2.4 3.4z" fill="#fff"/></svg>
          (949) 555-0147
        </div>
        <div class="contact-line">
          <svg viewBox="0 0 10 10"><circle cx="5" cy="5" r="5" fill="#1b47a0"/><rect x="2.6" y="3.6" width="4.8" height="3" fill="#fff"/><rect x="3.4" y="2.4" width="3.2" height="1.4" fill="#fff"/></svg>
          (949) 555-0147
        </div>
      </div>
    </div>

    <section class="letter">
      <div class="recipient">Mr/s<br>First Name and Last Name<br>Company Name<br>Address</div>
      <p>Lorem Ipsum is simply dummy text of the printing and typesetting industry. Lorem Ipsum has been the industry's standard dummy text ever since the 1500s, when an unknown printer took a galley of type and scrambled it to make a type specimen book. It has survived not only five centuries, but also the leap into electronic typesetting, remaining essentially unchanged. It was popularised in the 1960s with the release of Dryline sheets containing Lorem Ipsum passages.</p>
      <p>The standard chunk of Lorem Ipsum used since the 1500s is reproduced below for those interested. Sections 1.10.32 and 1.10.33 from "de Finibus Bonorum et Malorum" by Quintor are also reproduced in their exact original form, accompanied by English versions from the 1914 translation by H. Fennick. Lorem ipsum dolor sit amet, consectetur adipiscing elit, sed do eiusmod tempor incididunt ut labore et dolore magna aliqua.</p>
      <p>It is a long established fact that a reader will be distracted by the readable content of a page when looking at its layout. The point of using Lorem Ipsum is that it has a more-or-less normal distribution of letters, as opposed to using 'Content here, content here', making it look like readable English. Many desktop publishing packages and web page editors now.</p>
      <div class="closing">Your Sincerely,</div>
      <div class="signature-area" role="img" aria-label="Handwritten signature"></div>
    </section>

    <section class="locations">
      <div class="location">PELMIR HQ<br>41827 Heron Bluff Lane, Suite 316<br>Laguna Niguel, CA 92677</div>
      <div class="location">PELMIR Elementary (K-5)<br>57314 Marbleton Ridge Road<br>Laguna Niguel, CA 92677</div>
      <div class="location">PELMIR College Prep (6-12)<br>46803 Sable Creek Way<br>San Juan Capistrano, CA 92675</div>
    </section>

    <svg class="footer" viewBox="0 0 618 72" preserveAspectRatio="none">
      <path d="M0 30 H205 C225 30 235 46 258 52 H618 V72 H0 Z" fill="var(--brand-blue)"/>
      <polygon points="250,49 345,44 348,44 258,49" fill="var(--green)"/>
      <polygon points="262,48 360,48 356,44 258,44" fill="var(--green)"/>
      <polygon points="364,48 462,48 458,44 360,44" fill="var(--sky)"/>
      <polygon points="466,48 540,48 536,44 462,44" fill="var(--yellow)"/>
      <polygon points="544,48 618,48 618,44 540,44" fill="var(--orange)"/>
    </svg>
    <div class="website">
      <svg viewBox="0 0 10 10"><circle cx="5" cy="5" r="4.3" fill="none" stroke="#fff" stroke-width="1.2"/><path d="M.8 5h8.4M5 .8c-2 2.4-2 6 0 8.4M5 .8c2 2.4 2 6 0 8.4" fill="none" stroke="#fff" stroke-width=".8"/></svg>
      www.pelmir-learn.example
    </div>
  </main>
</body>
</html>
```